Business Card Design

The business is a mobile physiotherapy, personal training and massage business located on the gold coast. I would like a design that works well with my logo that I had recently created by a graphic design company.

I have a mock business card made from the prinwell website. This may help with the design.

Target Market(s)

Any age although specifically for 30+

Industry/Entity Type

Graphic Design

Contact Information for Business Card

Summit Motion Physio
Mobile Physiotherapy, Personal Training & Massage Service
Location: Gold Coast
Marcus Tellwin
Dr. of Physiotherapy & B. Ex. Science
e: summitmotionphysio@mailbox.example
w: www.summitmotionphysio.example
m: 0455 726 309

```html
<!DOCTYPE html>
<html lang="en">
<head>
<meta charset="utf-8">
<title>Summit Motion Physio – Business Card</title>
<link href="https://fonts.googleapis.com/css2?family=Open+Sans:wght@400;700&display=swap" rel="stylesheet">
<style>
  :root {
    --stage: #808080;
    --card-dark: #1b1a1c;
    --card-light: #ffffff;
    --brand-red: #b5121b;
    --text-red: #a8141c;
    --figure-red: #c4141f;
    --figure-dark: #1c1c1c;
  }
  html, body {
    margin: 0;
    padding: 0;
    width: 1200px;
    height: 434px;
    overflow: hidden;
    background: var(--stage);
    font-family: "Open Sans", Arial, sans-serif;
  }
  .canvas {
    position: relative;
    width: 1200px;
    height: 434px;
  }
  .card {
    position: absolute;
    top: 47px;
    width: 511px;
    height: 315px;
  }
  .card--back {
    left: 73px;
    background: var(--card-dark);
  }
  .card--front {
    left: 606px;
    background: var(--card-light);
    overflow: hidden;
  }
  .brand-name {
    position: absolute;
    margin: 0;
    font-weight: 700;
    color: var(--brand-red);
    white-space: nowrap;
  }
  .card--back .brand-name {
    left: 0;
    right: 0;
    top: 148px;
    text-align: center;
    font-size: 26px;
  }
  .card--front .brand-name {
    left: 34px;
    top: 64px;
    font-size: 22px;
  }
  .tagline {
    position: absolute;
    left: 34px;
    top: 137px;
    margin: 0;
    font-size: 12.5px;
    line-height: 19px;
    color: var(--text-red);
    white-space: nowrap;
  }
  .practitioner {
    position: absolute;
    left: 34px;
    top: 195px;
    margin: 0;
    font-size: 11px;
    line-height: 17px;
    color: var(--text-red);
    white-space: nowrap;
  }
  .contact-list {
    position: absolute;
    left: 34px;
    top: 235px;
    margin: 0;
    padding: 0;
    list-style: none;
    font-size: 11px;
    line-height: 16px;
    color: var(--text-red);
    white-space: nowrap;
  }
  .contact-list li {
    display: flex;
    align-items: center;
    gap: 8px;
  }
  .contact-icon {
    width: 9px;
    height: 9px;
    flex: none;
  }
  .hero-figure {
    position: absolute;
    left: 312px;
    top: 40px;
    width: 199px;
    height: 260px;
  }
</style>
</head>
<body>
  <main class="canvas">
    <section class="card card--back" aria-label="Card back">
      <p class="brand-name">Summit Motion Physio</p>
    </section>

    <section class="card card--front" aria-label="Card front">
      <p class="brand-name">Summit Motion Physio</p>

      <p class="tagline">Summit Motion Physio Mobile Physiotherapy,<br>Massage and Personal Training Service</p>

      <p class="practitioner">Gold Coast Marcus Tellwin Dr. of Physiotherapy<br>&amp; B. Ex. Science</p>

      <ul class="contact-list">
        <li>
          <svg class="contact-icon" viewBox="0 0 10 10" aria-hidden="true"><text x="0" y="8.5" font-size="10" fill="currentColor" font-family="Open Sans, sans-serif">@</text></svg>
          summitmotionphysio@mailbox.example
        </li>
        <li>
          <svg class="contact-icon" viewBox="0 0 10 10" aria-hidden="true"><circle cx="5" cy="5" r="4.5" fill="currentColor"/><path d="M5 1.5v7M1.5 5h7" stroke="#fff" stroke-width="1"/></svg>
          www.summitmotionphysio.example
        </li>
        <li>
          <svg class="contact-icon" viewBox="0 0 10 10" aria-hidden="true"><rect x="2" y="0.5" width="6" height="9" rx="1" fill="currentColor"/><rect x="3" y="1.8" width="4" height="5.5" fill="#fff"/></svg>
          0455 726 309
        </li>
      </ul>

      <svg class="hero-figure" role="img" aria-label="Illustration of a sprinting athlete in red and black with a sweeping red arc" viewBox="0 0 199 260">
        <defs>
          <linearGradient id="figureTone" x1="1" y1="0" x2="0" y2="1">
            <stop offset="0" stop-color="#c4141f"/>
            <stop offset="0.45" stop-color="#8f1218"/>
            <stop offset="1" stop-color="#1c1c1c"/>
          </linearGradient>
        </defs>
        <rect x="0" y="0" width="199" height="260" rx="14" fill="url(#figureTone)" opacity="0.85"/>
      </svg>
    </section>
  </main>
</body>
</html>
```